ORVILMA card Technical Architecture

Hello everyone ORVILMA: It is a consulting firm in Architecture and Construction. I require a card duplexing, sober, elegant, classic but not boring. Update 1: Use the following data for the card. Name: Rodrigo Salinas Tomás Quevedo Position: COO Twitter: @orvilmaAT Homepage: orvilma.com home address not include the participation of all thank you.

Target Market(s)

Construction companies, Architects and Consulting Engineers

Industry/Entity Type

Consulting

Contact Information for Business Card

Los campos que debe tener:
Nombre, Cargo, email, homepage y twitter

Font styles to use
Serif
Sans Serif
Other font styles liked:
• Me gustan playfair display, open sans y roboto, pero estoy sujeto a sus propuestas

Requirements
Must have
• Colors: Present combined proposals in white, red, gray and black Update 1: The two names must be clearly differentiated from the two surnames
Nice to have
• They are free to present their best proposals. I will bring them immediate feedback to the extent you can go see their designs. Complete data for card and logo files will give the winner the

```html
<!DOCTYPE html>
<html lang="en">
<head>
<meta charset="utf-8">
<title>ORVILMA – Business Card, Front and Back</title>
<link rel="stylesheet" href="https://fonts.googleapis.com/css2?family=Open+Sans:wght@400;600;700&family=Montserrat:wght@300;400&display=swap">
<style>
  :root {
    --stage-bg: #000000;
    --card-deep: #740003;
    --card-bright: #c3001a;
    --card-edge: #7c0009;
    --ink-light: #ffffff;
    --mark-panel: #ffffff;
  }
  * { margin: 0; padding: 0; box-sizing: border-box; }
  html, body {
    width: 1200px; height: 900px; overflow: hidden;
    background: var(--stage-bg);
  }
  .stage { position: relative; width: 1200px; height: 900px; }

  .card {
    position: absolute; top: 200px; width: 310px; height: 502px;
    overflow: hidden; color: var(--ink-light);
  }

  /* Front: contact side */
  .card--front {
    left: 265px;
    background: var(--card-deep);
    border-radius: 56px 0 56px 0;
    font-family: "Open Sans", Arial, sans-serif;
  }
  .mark-panel {
    position: absolute; top: 0; right: 0; width: 120px; height: 186px;
    background: var(--mark-panel);
    display: flex; align-items: center; justify-content: center;
  }
  .mark-panel__name {
    font-family: "Open Sans", Arial, sans-serif;
    font-weight: 700; font-size: 18px; letter-spacing: 1px;
    color: var(--card-deep);
  }
  .holder { position: absolute; left: 25px; top: 260px; }
  .holder__name { font-size: 16px; font-weight: 700; line-height: 22px; }
  .holder__role { font-size: 12.5px; font-weight: 400; line-height: 18px; }

  .contact-list { position: absolute; left: 25px; top: 338px; list-style: none; }
  .contact-list li {
    display: flex; align-items: center; gap: 8px;
    font-size: 13px; line-height: 19px; height: 19px;
  }
  .contact-list svg { width: 13px; height: 13px; flex: none; }

  .social { position: absolute; left: 25px; top: 420px; display: flex; align-items: center; gap: 8px; font-size: 17px; }
  .social__square { width: 15px; height: 15px; background: var(--ink-light); border-radius: 2px; }

  /* Back: brand side */
  .card--back {
    left: 641px;
    background: radial-gradient(circle at 30% 45%, var(--card-bright) 0%, #a8000f 45%, var(--card-edge) 100%);
    border-radius: 0 56px 0 56px;
  }
  .brand-dot {
    position: absolute; left: 62px; top: 226px; width: 30px; height: 30px;
    border-radius: 50%; background: var(--ink-light);
  }
  .brand-name, .brand-tagline {
    position: absolute; white-space: nowrap;
    transform: translate(-50%, -50%) rotate(-90deg);
    font-family: "Montserrat", Arial, sans-serif;
  }
  .brand-name {
    left: 188px; top: 258px;
    font-size: 60px; font-weight: 300; letter-spacing: 14px;
  }
  .brand-rule {
    position: absolute; left: 217px; top: 55px; width: 1.5px; height: 410px;
    background: var(--ink-light);
  }
  .brand-tagline {
    left: 236px; top: 257px;
    font-size: 16px; font-weight: 400; letter-spacing: 6.2px;
  }
</style>
</head>
<body>
<main class="stage">

  <section class="card card--front" aria-label="Card front">
    <div class="mark-panel"><span class="mark-panel__name">ORVILMA</span></div>

    <div class="holder">
      <p class="holder__name">Selim Arkan, BSc.</p>
      <p class="holder__role">Owner and Creative Superhero</p>
    </div>

    <ul class="contact-list">
      <li>
        <svg viewBox="0 0 13 13" aria-hidden="true"><rect width="13" height="13" rx="1.5" fill="#fff"/><path d="M3.5 2.8c.4-.3.9-.2 1.1.2l.7 1.3c.2.4 0 .8-.3 1l-.4.3c.4 1 1.2 1.8 2.2 2.2l.3-.4c.2-.3.7-.5 1-.3l1.3.7c.4.2.5.7.2 1.1l-.6.7c-.4.4-1 .5-1.5.3C5.5 9.2 3.8 7.5 3 5.6c-.2-.5-.1-1.1.3-1.5z" fill="#740003"/></svg>
        <span>43 (0) 612 305 91 28</span>
      </li>
      <li>
        <svg viewBox="0 0 13 13" aria-hidden="true"><rect width="13" height="13" rx="1.5" fill="#fff"/><rect x="2.8" y="3.8" width="7.4" height="5.4" fill="none" stroke="#740003" stroke-width="1.1"/><path d="M2.8 3.8l3.7 3 3.7-3" fill="none" stroke="#740003" stroke-width="1.1"/></svg>
        <span>info@orvilma.com</span>
      </li>
      <li>
        <svg viewBox="0 0 13 13" aria-hidden="true"><rect width="13" height="13" rx="1.5" fill="#fff"/><circle cx="6.5" cy="6.5" r="3.8" fill="none" stroke="#740003" stroke-width="1.1"/><path d="M2.7 6.5h7.6M6.5 2.7c-1.6 2.3-1.6 5.3 0 7.6M6.5 2.7c1.6 2.3 1.6 5.3 0 7.6" fill="none" stroke="#740003" stroke-width="0.9"/></svg>
        <span>www.orvilma.com</span>
      </li>
    </ul>

    <div class="social"><span class="social__square" aria-hidden="true"></span><span>/orvilmaAT</span></div>
  </section>

  <section class="card card--back" aria-label="Card back">
    <span class="brand-dot" aria-hidden="true"></span>
    <p class="brand-name">ORVILMA</p>
    <span class="brand-rule" aria-hidden="true"></span>
    <p class="brand-tagline">ARQUITECTURA TÉCNICA</p>
  </section>

</main>
</body>
</html>
```